以前から店舗のすぐ近くを通る幹線道路沿いに看板を出していました。
現在の看板は【3.6mx2.7m】ですが、弊社の看板の下の枠にちょうど空きが出たため上下をつなげて今回【3.6mx5.4m】の大型で製作し直すことになりました。

現在使用中の看板デザインは社内で話し合って作りました。
パソコンや紙で確認していた時は良いと思ったのですが、実際出来上がってみると思ったより文字も小さく遠くからでは内容がわかりづらかったです。
そんな失敗もあり、さらに今回はサイズが2倍になるということもあってプロの方にお願いした方が良いモノが出来上がると思いご依頼させて頂くことになりました。

製作は看板設置会社で行うのでデザインをお願いしたいと思います。

【看板の目的】
当店の認知度拡大と来店促進及びオーダーメイドまくらの販促強化

【設置場所と看板イメージ】
設置場所は車の交通量も多く、看板横のコンビニも車での来店が非常に多い場所です。
(設置場所の画像も添付ファイルに入れています。)
隣に別会社の看板もあるためそれよりも目立つ様にしたいです。
ただ、取り扱っている商品が中~高価格帯のためあまりハデすぎると店舗のイメージには合わないかもしれません。
店舗の「癒し」や「ナチュラル」といったイメージで目立つ看板にしたいという非常に矛盾した要望で恐縮ですが宜しくお願い致します。
看板サイズ:幅3.6mx高さ5.4m【2分割(幅3.6mx高さ2.7mx2枚を上下に設置)】
※看板設置場所の条件で看板本体は上下2分割で設置しないといけません。
※上と下の隙間は10~15cm程の予定です。
※隙間は空きますがデザイン的におかしくなければ一体型の大きなデザインでも
良いかと思っています。

【必ず載せて頂きたい内容】
・店舗ロゴ(添付ファイル有)もしくは店名(寝具の専門店ほしぞの)
・この信号を左折(意味が伝われば表現や言い方は多少変わっても大丈夫です。)
・「オーダーメイドまくら」という文言
(正式には「オーダーメイドまくら」ですが「オーダーまくら」でも可)

【看板設置の目的】
・当店と当店のオーダーメイドまくらの認知度向上と来店促進

【素材について】
・使用できるイメージ画像をいくつか添付ファイルに入れています。
使用した方がいいかどうかも含めてご判断頂ければと思います。
こちらのサービスを初めて利用するのでやり取りが不慣れなところもあるかと思いますが宜しくお願い致します。

今回はこちらのデザインに決定させて頂きました。
伝えたいポイントがわかりやすく表現されているのと、他の看板などと並んだ時にも目立つデザインが社内の選定で選ばれた理由です。
修正にも迅速、丁寧に対応して頂きありがとうございました。

今回は弊社のコンペに多数の方にご参加頂き誠にありがとうございました。
今回初めてクラフタスさんを利用させて頂きましたが、みなさんからすばらしいご提案をたくさん頂き、最後までスタッフみんなで非常に悩みました。
今後も店舗運営上、色々な部分でクラフタスさんを利用させて頂こうと思っていますので今後も宜しくお願い致します。

```html
<!DOCTYPE html>
<html lang="ja">
<head>
<meta charset="utf-8">
<title>寝具の専門店ほしぞの 看板</title>
<link rel="stylesheet" href="https://fonts.googleapis.com/css2?family=M+PLUS+Rounded+1c:wght@500;800&family=Noto+Serif+JP:wght@900&display=swap">
<style>
  :root {
    --bg: #dcedf6;
    --frame: #c9dde8;
    --magenta: #e4097f;
    --white: #ffffff;
    --ink: #1e1e1e;
    --post: #9aa3a8;
    --photo-top: #e9ecef;
    --photo-bottom: #c9ced3;
  }
  * { margin: 0; padding: 0; box-sizing: border-box; }
  html, body { width: 846px; height: 1200px; overflow: hidden; background: var(--bg); }
  .canvas { position: relative; width: 846px; height: 1200px; background: var(--bg); border: 2px solid var(--frame); }
  .board-top {
    position: absolute; left: 56px; top: 28px; width: 740px; height: 325px;
    background: var(--white);
  }
  .brand-mark {
    position: absolute; left: 31px; top: 85px; width: 190px; height: 183px;
    border: 3px solid var(--ink);
  }
  .brand-divider {
    position: absolute; left: 236px; top: 85px; width: 3px; height: 183px; background: var(--magenta);
  }
  .brand-tagline {
    position: absolute; left: 256px; top: 96px;
    font-family: "M PLUS Rounded 1c", sans-serif; font-weight: 500;
    font-size: 36px; line-height: 1.2; color: var(--magenta); letter-spacing: 2px; white-space: nowrap;
  }
  .brand-name {
    position: absolute; left: 252px; top: 150px;
    font-family: "M PLUS Rounded 1c", sans-serif; font-weight: 500;
    font-size: 108px; line-height: 1; color: var(--magenta); letter-spacing: 0; white-space: nowrap;
  }
  .post { position: absolute; top: 353px; width: 18px; height: 28px; background: var(--post); }
  .post-left { left: 160px; }
  .post-right { left: 680px; }
  .board-bottom {
    position: absolute; left: 56px; top: 381px; width: 740px; height: 762px;
    background: var(--magenta);
  }
  .promise {
    position: absolute; left: 70px; top: 84px; width: 600px; height: 112px;
    background: var(--white);
    display: flex; align-items: center; justify-content: center;
    font-family: "Noto Serif JP", serif; font-weight: 900;
    font-size: 68px; line-height: 1; color: var(--magenta); letter-spacing: 6px; white-space: nowrap;
  }
  .slash { position: absolute; top: 84px; width: 12px; height: 112px; background: var(--white); }
  .slash-left { left: 38px; transform: skewX(20deg); }
  .slash-right { left: 690px; transform: skewX(-20deg); }
  .product {
    position: absolute; left: 57px; top: 254px; width: 626px; height: 400px;
    background: var(--white); overflow: hidden;
  }
  .product-title {
    position: absolute; left: 0; right: 0; top: 18px; text-align: center;
    font-family: "M PLUS Rounded 1c", sans-serif; font-weight: 800;
    font-size: 52px; line-height: 80px; color: var(--ink); white-space: nowrap;
  }
  .product-title .accent { font-size: 70px; }
  .product-photo {
    position: absolute; left: 0; right: 0; top: 114px; bottom: 0;
    background: linear-gradient(180deg, var(--photo-top), var(--photo-bottom));
  }
  .direction {
    position: absolute; left: 0; right: 0; top: 662px; height: 92px;
  }
  .turn-arrow { position: absolute; left: 24px; top: 6px; width: 120px; height: 82px; }
  .direction-text {
    position: absolute; left: 166px; top: 0; height: 92px;
    display: flex; align-items: center;
    font-family: "M PLUS Rounded 1c", sans-serif; font-weight: 800;
    font-size: 46px; line-height: 1; color: var(--white); white-space: nowrap;
  }
  .direction-text .accent { font-family: "Noto Serif JP", serif; font-weight: 900; font-size: 80px; line-height: 1; margin-left: 6px; }
</style>
</head>
<body>
<div class="canvas">
  <section class="board-top">
    <div class="brand-mark"></div>
    <div class="brand-divider"></div>
    <p class="brand-tagline">寝具の専門店</p>
    <h1 class="brand-name">ほしぞの</h1>
  </section>

  <div class="post post-left"></div>
  <div class="post post-right"></div>

  <section class="board-bottom">
    <div class="slash slash-left"></div>
    <p class="promise">永久無料調整</p>
    <div class="slash slash-right"></div>

    <div class="product">
      <h2 class="product-title">オーダーメイド<span class="accent">まくら</span></h2>
      <div class="product-photo" role="img" aria-label="枕の高さを調整してもらい横になる女性の写真"></div>
    </div>

    <div class="direction">
      <svg class="turn-arrow" viewBox="0 0 120 82" aria-hidden="true">
        <path d="M104 82 V40 Q104 28 92 28 H42" fill="none" stroke="#ffffff" stroke-width="16" stroke-linecap="round"/>
        <polygon points="6,28 46,2 46,54" fill="#ffffff"/>
      </svg>
      <p class="direction-text">この信号を<span class="accent">左折</span></p>
    </div>
  </section>
</div>
</body>
</html>
```